Point of Sale Systems Web Design Project

I need a complete redesign of my existing website. I sell point of sale systems and need to seamlessly combine the features, products and services of several companies I represent. The current site is at www.tillgrovehub.com. The new site will be rebranded as www.VendaloFlo.com. I will be adding products from www.quillpoint.com, www.brenvale.com, www.dashkettle.com as well as other similar products and services such as http://orbanfield.com/homepage_USA.html

The new tag line will be:
Electronic Payment Systems Made FLO!
Updates

I have made a change to the website name. The new name will be VendaloFlo.com. I look forward to seeing the designs. Please see http://www.tovra.com.au/index.html for the inspiration behind the new name. I am also going to increase the budget for this project. Thank you

Target Market(s)

These are products and services for business owners. We provide Credit Card Processing Equipment and Processing Services to Retail, Restaurant, Home-based, and Internet businesses.

Industry/Entity Type

Electronic

Requirements
Must have
• Visitors need to be able to view video demos and download PDF documents. Site should be easy to update with new products or services.
Nice to have
• Designs I like: http://www.greyloftworks.com, http://www.pinewhistlegoods.com, http://www.lattiscobridge.com/

```html
<!DOCTYPE html>
<html lang="en">
<head>
<meta charset="utf-8">
<title>VendaloFlo.com – Electronic Payment Solutions</title>
<link rel="stylesheet" href="https://fonts.googleapis.com/css2?family=Didact+Gothic&family=Ubuntu:wght@500;700&display=swap">
<style>
:root{
  --canvas:#cfe6f7;
  --page:#ffffff;
  --header-dark:#0a86d6;
  --header-light:#2cbaf2;
  --navy:#0b2f5c;
  --nav-band:#e3f0fa;
  --ink:#2f2f2f;
  --ink-soft:#555555;
  --heading-grey:#575757;
  --accent-blue:#0aa3e6;
  --accent-red:#c0271f;
  --button-blue:#d3eafa;
  --button-text:#2d3a48;
  --soft-button:#d8ecfa;
  --line:#d6dde4;
  --field-border:#dfe6ec;
  --bottom-top:#ffffff;
  --bottom-end:#cfe7f8;
}
*{box-sizing:border-box;margin:0;padding:0}
html,body{width:1112px;height:1200px;overflow:hidden;background:var(--canvas)}
body{font-family:"Didact Gothic",sans-serif;color:var(--ink)}
.stage{position:absolute;left:0;top:0;width:1073px;height:1157px;transform:scale(1.0363,1.0372);transform-origin:0 0}
.stage *{position:absolute}
.stage br{position:static}
.layer{left:0;top:0;width:1073px;height:1157px}
.page{left:41px;top:2px;width:992px;height:1140px;background:var(--page);box-shadow:0 2px 6px rgba(0,60,110,.25)}
.masthead{left:50px;top:10px;width:975px;height:93px;border:3px solid #fff;border-radius:5px;background:linear-gradient(90deg,var(--header-dark),var(--header-light) 35%,var(--header-dark) 70%,var(--header-light));box-shadow:0 1px 3px rgba(0,0,0,.2)}
.masthead-texture{left:230px;top:0;width:360px;height:87px;background:linear-gradient(100deg,rgba(255,255,255,0),rgba(255,255,255,.28) 50%,rgba(255,255,255,0))}
.brand{left:15px;top:26px;font-size:26px;color:var(--navy);white-space:nowrap}
.phone{left:615px;top:26px;font-size:26px;color:#fff;letter-spacing:.5px;white-space:nowrap}
.social{left:820px;top:31px;width:145px;height:24px;display:flex;gap:7px}
.social span,.social svg{position:static;display:block;width:22px;height:22px;border-radius:4px;background:rgba(255,255,255,.85)}
.social svg{background:none}
.nav-band{left:41px;top:104px;width:992px;height:32px;background:var(--nav-band)}
.nav{font-family:"Ubuntu",sans-serif;font-weight:700;font-size:15px;color:#474747;top:110px;letter-spacing:.4px;white-space:nowrap}
.hero-art{left:41px;top:146px;width:326px;height:318px;border-radius:0 6px 6px 0;background:linear-gradient(150deg,#bfe3f7,#2e9be0 55%,#1366b8)}
.tagline{left:399px;top:163px;font-family:"Ubuntu",sans-serif;font-weight:700;font-size:27px;color:var(--heading-grey);letter-spacing:1px;white-space:nowrap}
.subline{left:399px;top:227px;font-family:"Ubuntu",sans-serif;font-weight:700;font-size:28px;color:var(--accent-blue);letter-spacing:.8px;white-space:nowrap}
.hero-copy{left:399px;top:264px;width:610px;font-size:14px;line-height:16px;color:#333}
.cta{top:413px;width:148px;height:38px;background:var(--button-blue);border-radius:2px;box-shadow:1px 2px 2px rgba(0,0,0,.15);font-family:"Ubuntu",sans-serif;font-weight:700;font-size:13px;line-height:14px;color:var(--button-text);padding:5px 0 0 20px;letter-spacing:.4px}
.cta-label{left:20px;top:5px;white-space:nowrap}
.cta svg{right:6px;top:3px}
.pdf-icon{left:965px;top:407px}
.pdf-label{left:952px;top:439px;font-size:9px;color:#444;white-space:nowrap}
.hero-rule{left:41px;top:468px;width:830px;height:2px;background:linear-gradient(90deg,var(--line),rgba(214,221,228,0))}
.col-rule{top:510px;width:0;height:258px;border-left:1px dashed #c9c9c9}
.col-title{font-family:"Ubuntu",sans-serif;font-weight:700;font-size:16px;line-height:20px;color:#222;letter-spacing:.5px}
.col-copy{font-size:13px;line-height:19px;color:var(--ink-soft)}
.col-art{border-radius:3px}
.video-btn{top:738px;width:94px;height:25px;background:var(--soft-button);border-radius:2px;font-family:"Ubuntu",sans-serif;font-weight:700;font-size:10px;color:#fff;letter-spacing:.3px}
.video-label{left:8px;top:6px;white-space:nowrap}
.video-btn svg{right:4px;top:4px}
.partner-name{left:726px;top:614px;font-size:19px;color:#8a9a4a;white-space:nowrap}
.lower{left:41px;top:804px;width:992px;height:290px;background:linear-gradient(180deg,var(--bottom-top),var(--bottom-end))}
.lower-rule{left:65px;top:803px;width:560px;height:2px;background:linear-gradient(90deg,rgba(214,221,228,0),var(--line) 20%,rgba(214,221,228,0))}
.quote-title{left:226px;top:841px;font-family:"Ubuntu",sans-serif;font-weight:700;font-size:17px;color:var(--accent-red);white-space:nowrap}
.field-label{left:77px;font-size:12px;color:#333;white-space:nowrap}
.field{left:224px;width:193px;height:21px;background:#fff;border:1px solid var(--field-border)}
.select-text{left:6px;top:3px;font-size:11px;color:#444}
.select-arrow{right:2px;top:2px;width:16px;height:15px;background:#e4e6e8}
.submit{left:224px;top:1041px;font-size:16px;color:var(--accent-red);white-space:nowrap}
.split-rule{left:470px;top:830px;width:1px;height:240px;background:linear-gradient(180deg,rgba(200,210,220,0),#d3dde6,rgba(200,210,220,0))}
.news-art{left:527px;width:123px;border:1px solid #c8d0d6;background:#fff}
.news-title{left:689px;font-family:"Ubuntu",sans-serif;font-weight:700;font-size:16px;color:var(--accent-blue);letter-spacing:.5px;white-space:nowrap}
.news-date{left:689px;font-weight:700;font-size:11px;color:#222;font-family:"Ubuntu",sans-serif;letter-spacing:.4px;white-space:nowrap}
.news-copy{left:689px;width:310px;font-size:12px;line-height:15px;color:#333;letter-spacing:.3px}
.more{left:689px;font-family:"Ubuntu",sans-serif;font-weight:700;font-size:11px;color:#d31d15;letter-spacing:.4px;white-space:nowrap}
.footer{left:41px;top:1094px;width:992px;height:48px;background:var(--canvas);border-top:2px solid #fff}
.partner-badge{left:187px;top:9px;width:104px;height:28px;border-radius:4px;background:#b9d3c8}
.copy-mark{left:317px;top:8px}
.legal{left:342px;top:7px;font-size:12px;line-height:15px;color:#333;white-space:nowrap}
</style>
</head>
<body>
<div class="stage">
  <div class="page"></div>

  <header class="masthead">
    <div class="masthead-texture" role="img" aria-label="Faint pattern of binary digits across the header"></div>
    <div class="brand">VendaloFlo.com</div>
    <div class="phone">888-555-0142</div>
    <div class="social" aria-label="Social links">
      <span></span><span></span><span></span><span></span>
      <svg viewBox="0 0 22 22" aria-label="Email"><rect x="1" y="4" width="20" height="14" fill="none" stroke="#fff" stroke-width="1.6"/><path d="M1 4l10 8 10-8" fill="none" stroke="#fff" stroke-width="1.6"/></svg>
    </div>
  </header>

  <div class="nav-band"></div>
  <nav class="layer">
    <span class="nav" style="left:399px">Home</span>
    <span class="nav" style="left:490px">About</span>
    <span class="nav" style="left:583px">Solutions</span>
    <span class="nav" style="left:703px">Services</span>
    <span class="nav" style="left:816px">Equipment</span>
    <span class="nav" style="left:945px">Contact</span>
  </nav>

  <section class="hero layer">
    <div class="hero-art" role="img" aria-label="Illustration of three stacked blue credit cards"></div>
    <h1 class="tagline">Electronic Payment Solutions Made FLO!</h1>
    <h2 class="subline">POS Technology, Systems And Solutions</h2>
    <p class="hero-copy">No storefront. No problem. Do you have a PC or Laptop connected to the internet?<br>Start processing credit card transactions from any computer with an internet connection.<br>Manually process mail and telephone credit&nbsp; card transactions or swipe card via a USB card swiper. Just like a traditional terminal, but with the added flexubility of giving you access from any interne connection&nbsp; in the world.<br>There’s no hardware to purchase&nbsp; or soft to download. It’s flexible, low-cost and trouble free.</p>
    <div class="cta" style="left:402px"><span class="cta-label">Virtual<br>Teminal</span></div>
    <div class="cta" style="left:575px"><span class="cta-label">Process<br>Payments</span>
      <svg width="32" height="32" viewBox="0 0 32 32"><circle cx="16" cy="16" r="14" fill="#fff" stroke="#b9dcf2" stroke-width="2"/><path d="M13 9l7 7-7 7" fill="none" stroke="#1a8fd8" stroke-width="3"/></svg>
    </div>
    <svg class="pdf-icon" width="26" height="28" viewBox="0 0 26 28" aria-label="PDF document"><path d="M2 1h16l6 6v20H2z" fill="#fff" stroke="#c9302c" stroke-width="1.5"/><rect x="5" y="11" width="16" height="9" fill="#d9342b"/></svg>
    <span class="pdf-label">PDF&nbsp; Details</span>
    <div class="hero-rule"></div>
  </section>

  <section class="features layer">
    <div class="col-rule" style="left:378px"></div>
    <div class="col-rule" style="left:706px"></div>

    <h3 class="col-title" style="left:77px;top:506px;width:290px">Brenvale Salon</h3>
    <p class="col-copy" style="left:77px;top:529px;width:292px">software does everything you've come to expect rom a salon software POS system - and so much more. The simple touch screen and finger-friendly salon software design will have you moving at salon speed in no time.</p>
    <div class="col-art" style="left:128px;top:638px;width:150px;height:82px;background:linear-gradient(135deg,#d9d9d9,#3a3a3a 60%,#6d6d6d)" role="img" aria-label="Salon POS terminal with printer and card reader"></div>
    <div class="video-btn" style="left:79px"><span class="video-label">View video</span>
      <svg width="17" height="17" viewBox="0 0 17 17"><circle cx="8.5" cy="8.5" r="7.5" fill="#fff"/><path d="M7 5l4 3.5L7 12" fill="none" stroke="#d31d15" stroke-width="1.8"/></svg>
    </div>

    <h3 class="col-title" style="left:399px;top:506px;width:290px">Complet and Affordable POS Solutions for Retai and Hospitality Merchants!</h3>
    <p class="col-copy" style="left:399px;top:578px;width:285px">Choose from a variety of accessories that are designed specifically with the retail and restaurante environment!</p>
    <div class="col-art" style="left:462px;top:648px;width:150px;height:72px;background:linear-gradient(135deg,#0e63c4,#3d9ae8 50%,#0a4fa0)" role="img" aria-label="Retail POS monitor, keypad and receipt printer"></div>
    <div class="video-btn" style="left:401px"><span class="video-label">View video</span>
      <svg width="17" height="17" viewBox="0 0 17 17"><circle cx="8.5" cy="8.5" r="7.5" fill="#fff"/><path d="M7 5l4 3.5L7 12" fill="none" stroke="#d31d15" stroke-width="1.8"/></svg>
    </div>

    <h3 class="col-title" style="left:726px;top:506px;width:260px">Accepting Credit Cards Has Never Been Easier.</h3>
    <p class="col-copy" style="left:726px;top:550px;width:275px">Dashkettle is a free app and free credit card reader that transforms your smartphone into a mobile point-of-sale terminal.</p>
    <div class="partner-name">Dashkettle</div>
    <div class="col-art" style="left:777px;top:654px;width:153px;height:76px;background:linear-gradient(135deg,#e8ece9,#7fae3c 45%,#3a3a3a)" role="img" aria-label="Smartphones with clip-on card readers"></div>
    <div class="video-btn" style="left:728px"><span class="video-label">View video</span>
      <svg width="17" height="17" viewBox="0 0 17 17"><circle cx="8.5" cy="8.5" r="7.5" fill="#fff"/><path d="M7 5l4 3.5L7 12" fill="none" stroke="#d31d15" stroke-width="1.8"/></svg>
    </div>
  </section>

  <section class="lower"></section>
  <div class="lower-rule"></div>

  <form class="quote layer">
    <h3 class="quote-title">Get a FREE quote!</h3>
    <label class="field-label" style="top:877px">Full name:</label>
    <label class="field-label" style="top:900px">Email:</label>
    <label class="field-label" style="top:923px">Phone:</label>
    <label class="field-label" style="top:942px">Type of inquires:</label>
    <label class="field-label" style="top:1005px">Additional information:</label>
    <div class="field" style="top:868px"></div>
    <div class="field" style="top:891px"></div>
    <div class="field" style="top:914px"></div>
    <div class="field" style="top:937px;background:#f1f2f3"><span class="select-text">Select</span><span class="select-arrow"><svg width="16" height="15" viewBox="0 0 16 15" style="left:0;top:0"><path d="M4 5h8l-4 5z" fill="#888"/></svg></span></div>
    <div class="field" style="top:965px;height:68px"></div>
    <span class="submit">Get Quote Now!</span>
  </form>

  <div class="split-rule"></div>

  <article class="news layer">
    <div class="news-art" style="top:830px;height:97px"><div style="left:4px;top:4px;width:113px;height:87px;background:linear-gradient(135deg,#d9e7f5,#3c7fd0 50%,#c4322b)" role="img" aria-label="Fanned stack of gift cards"></div></div>
    <h4 class="news-title" style="top:828px">Gift Cards</h4>
    <span class="news-date" style="top:853px">1.06.2011</span>
    <p class="news-copy" style="top:874px">Suspendisse nibh pede, ultrices vitae, Itrices nec... Nam et augue. Sed a elit. Ut vel massa. Suspendisse nibh pede ultrices vitae, Itrices nec..</p>
    <span class="more" style="top:926px">Learn more ...</span>

    <div class="news-art" style="top:968px;height:96px;border:none"><div style="left:0;top:0;width:123px;height:96px;background:linear-gradient(135deg,#8c7a66,#e3ddd5 55%,#9a8b78)" role="img" aria-label="Stack of cards on a desk"></div></div>
    <h4 class="news-title" style="top:966px">Merchant Cash Advance</h4>
    <span class="news-date" style="top:984px">3.06.2011</span>
    <p class="news-copy" style="top:1004px">Suspendisse nibh pede, ultrices vitae, Itrices nec... Nam et augue. Sed a elit. Ut vel massa. Suspendisse nibh pede ultrices vitae, Itrices nec..</p>
    <span class="more" style="top:1054px">Learn more ...</span>
  </article>

  <footer class="footer">
    <div class="partner-badge"></div>
    <svg class="copy-mark" width="16" height="16" viewBox="0 0 16 16"><circle cx="8" cy="8" r="6.5" fill="none" stroke="#333" stroke-width="1.3"/><path d="M10.3 6a3 3 0 1 0 0 4" fill="none" stroke="#333" stroke-width="1.3"/></svg>
    <p class="legal">Summit Acceptance Group Registered Sales Agent for Northpay Processing Inc.<br>Member Bank: Harlow Ridge Bank N.A., Cedar Hollow, CA - Member.FDIC</p>
  </footer>
</div>
</body>
</html>
```